New concept travel "Fun" for young people !
----- Google Translate ----
With our skills, our agency was the first to develop spring break concepts in French-speaking Belgium by bringing together hundreds of students in Spain to celebrate!
Following a concern for health, our usual graphic designer can not take care of our achievements.
We are looking for a person in the long term (= serious work, contact exchanges and other "contracts").
We will also need a facebook cover and a single-sided A4 poster.
The name of the concept is GOLDEN DRIFT.
You will be free to create a beautiful new logo of course.
This one could possibly be put on future t-shirts for our staff of animators during the trip or offered to the public!
Here is the job to do:
- Objective NEW CONCEPT 2018 in Bulgaria -
We need a visual (efficient and dynamic flyer to attract a population between 21 and 35 years old.
Flyer idea: A6 landscape postcard format, vintage, with a beautiful visual on the front that makes you want and arouse curiosity (with title of the trip "GOLDEN DRIFT - Bulgaria 2018") and the mention "New Concept" with our logo MORELKA TRAVEL .
On the back, on the left half of the postcard: a sweet little word from a woman, the style "Hey ! Le soleil est bien là, les cocktails sont savoureux et l'ambiance incroyable ! On t'attends avec les filles ! Je t'embrasse. Nora" with a fake kiss (= smack).
On the right half, useful information to stay to know:
- du samedi 1 au samedi 8 septembre 2018
- Plage Morvane, Bulgarie
- Voyage "tout compris" : vol aller-retour, hôtel 4**** formule ALL INCLUSIVE, entrées en boites, cocktails offerts, beach party, ... & bien plus !
- prix : € 599,00 par personne en chambre double
- plus d'infos sur www.golden-drift.example ou au 0487 612 940
Here is the logo of our agency + some visuals of our last trip to Hungary (just to give you a little effect to feel ATTENTION I want something else here not copy please, please)
Good luck to everyone !

```html
<!DOCTYPE html>
<html lang="fr">
<head>
<meta charset="utf-8">
<title>Golden Drift – Bulgaria 2018 postcard</title>
<link rel="stylesheet" href="https://fonts.googleapis.com/css2?family=Caveat:wght@500&family=Pacifico&family=Zilla+Slab:wght@600;700&display=swap">
<style>
  :root{
    --bg:#e6e6e4;
    --paper:#fffdf8;
    --blush:#fbe3d6;
    --orange:#e8762b;
    --orange-deep:#c9561b;
    --ink-red:#b43a2a;
    --yellow:#f6d64a;
    --sand:#ecdcb8;
    --teal:#5cc4c0;
    --mint:#a9dfd2;
    --peach:#f6b896;
    --sky:#9fc7e6;
    --sea:#6fa9d6;
    --cream:#fff6e1;
    --lip:#e98aa4;
    --white:#ffffff;
  }
  *{box-sizing:border-box;margin:0;padding:0}
  html,body{width:1200px;height:851px;overflow:hidden;background:var(--bg)}
  .canvas{position:relative;width:1200px;height:851px}

  /* ---------- back of card ---------- */
  .card{position:absolute;width:560px;height:392px;box-shadow:0 4px 14px rgba(0,0,0,.18);overflow:hidden}
  .card-back{left:20px;top:230px;background:var(--paper)}
  .back-edge{position:absolute;left:0;top:0;bottom:0;width:10px;
    background:linear-gradient(var(--orange) 0 33%,var(--teal) 33% 66%,var(--yellow) 66%)}
  .back-wash{position:absolute;left:10px;top:0;width:270px;height:100%;background:var(--blush);opacity:.7;
    clip-path:polygon(0 0,100% 0,92% 20%,100% 40%,94% 62%,100% 82%,95% 100%,0 100%)}
  .divider{position:absolute;left:282px;top:40px;bottom:48px;width:2px;background:var(--orange);opacity:.5}
  .message{position:absolute;left:36px;top:40px;width:230px;font-family:"Caveat",cursive;font-size:19px;line-height:1.65;color:var(--ink-red)}
  .message p{margin-bottom:14px}
  .signature{position:absolute;left:190px;top:300px;font-family:"Caveat",cursive;font-size:20px;color:var(--ink-red)}
  .kiss{position:absolute;left:36px;top:282px;width:90px;height:56px;border-radius:50%;
    background:radial-gradient(ellipse at center,var(--lip),rgba(233,138,164,.25) 70%,transparent 72%)}
  .bottom-strip{position:absolute;left:10px;right:0;bottom:0;height:30px;background:var(--yellow);
    display:flex;align-items:center;justify-content:space-between;padding:0 24px 0 150px;
    font-family:"Zilla Slab",serif;font-weight:600;font-size:13px;color:var(--orange-deep)}

  .dates{position:absolute;left:300px;top:16px;width:170px;text-align:center;font-family:"Zilla Slab",serif;font-weight:700;font-size:20px;line-height:1.15;color:var(--orange)}
  .postmark{position:absolute;right:20px;top:16px;width:56px;height:66px;background:var(--peach);border:3px dashed var(--paper);outline:2px solid var(--orange)}
  .place-tag{position:absolute;left:318px;top:80px;width:128px;height:62px;background:var(--sand);transform:rotate(-3deg);
    border:2px dashed var(--orange);display:flex;flex-direction:column;justify-content:center;align-items:center;
    font-family:"Zilla Slab",serif;font-weight:700;font-size:15px;color:var(--orange);line-height:1.2}
  .concept-tag{position:absolute;left:290px;top:178px;width:100px;height:46px;background:var(--mint);transform:rotate(-28deg);
    border:2px dashed var(--orange);display:flex;align-items:center;justify-content:center;text-align:center;
    font-family:"Zilla Slab",serif;font-weight:700;font-size:13px;line-height:1.1;color:var(--orange)}
  .offer{position:absolute;left:398px;top:146px;width:152px;height:170px;background:var(--cream);transform:rotate(-8deg);
    border:2px dashed var(--orange);padding:28px 12px 10px}
  .offer-title{position:absolute;left:-8px;top:-16px;padding:4px 10px;background:var(--yellow);font-family:"Zilla Slab",serif;font-weight:700;font-size:18px;color:var(--orange)}
  .offer ul{list-style:none;font-family:"Zilla Slab",serif;font-weight:600;font-size:13px;line-height:1.35;color:var(--orange)}
  .offer .price{margin-top:6px;font-weight:700;font-size:14px;color:var(--orange-deep)}

  /* ---------- front of card ---------- */
  .card-front{left:620px;top:230px;background:var(--paper)}
  .stripe{position:absolute;top:0;height:100%}
  .s1{left:0;width:20px;background:var(--teal)}
  .s2{left:20px;width:14px;background:var(--peach)}
  .s3{right:0;width:16px;background:var(--yellow)}
  .s4{right:16px;width:12px;background:var(--mint)}
  .photo{position:absolute}
  .p-girl{left:34px;top:0;width:150px;height:140px;background:linear-gradient(140deg,#f0c9a0,#d88a52)}
  .p-palm{left:400px;top:0;width:130px;height:120px;background:linear-gradient(160deg,#7aa24a,#d6a04a)}
  .p-jump{left:34px;top:200px;width:150px;height:192px;background:linear-gradient(#f3e6c8,#e1b27c)}
  .p-friends{left:400px;top:170px;width:130px;height:222px;background:linear-gradient(#8fc4e4,#e6c39a)}
  .p-bag{left:440px;top:110px;width:90px;height:70px;background:var(--orange);transform:rotate(8deg)}
  .hero{position:absolute;left:190px;top:24px;width:204px;height:200px;background:linear-gradient(var(--sky),var(--sea) 60%,#e8d2aa);
    display:flex;flex-direction:column;align-items:center;justify-content:center;text-align:center;color:var(--white)}
  .hero-title{font-family:"Pacifico",cursive;font-size:34px;line-height:1.05;text-shadow:0 2px 0 rgba(0,0,0,.12)}
  .hero-sub{margin-top:8px;font-family:"Caveat",cursive;font-size:20px}
  .hero-photo{position:absolute;left:190px;top:224px;width:204px;height:100px;background:linear-gradient(#e9c89a,#c98e5a)}
  .band{position:absolute;left:190px;top:324px;width:204px;height:68px;
    background:repeating-linear-gradient(90deg,var(--peach) 0 24px,var(--mint) 24px 48px,var(--yellow) 48px 72px)}
  .star{position:absolute;left:162px;top:180px;width:30px;height:30px}
  .front-concept{position:absolute;left:150px;top:118px;width:84px;height:34px;background:var(--teal);transform:rotate(-18deg);
    border:2px dashed var(--white);display:flex;align-items:center;justify-content:center;text-align:center;
    font-family:"Zilla Slab",serif;font-weight:700;font-size:11px;line-height:1.05;color:var(--white)}
  .agency{position:absolute;left:204px;top:344px;width:176px;height:30px;background:var(--paper);
    display:flex;align-items:center;justify-content:center;gap:7px;
    font-family:"Zilla Slab",serif;font-weight:700;font-size:13px;letter-spacing:.5px;color:var(--orange)}
  .agency-dot{width:10px;height:10px;border-radius:50%;background:var(--orange)}
</style>
</head>
<body>
<main class="canvas">

  <section class="card card-back" aria-label="Postcard back">
    <div class="back-edge"></div>
    <div class="back-wash"></div>
    <div class="message">
      <p>Hey ! Le soleil est bien là, les cocktails sont savoureux et l'ambiance incroyable !</p>
      <p>On t'attends avec les filles !</p>
      <p>Je t'embrasse.</p>
    </div>
    <div class="kiss" role="img" aria-label="Lipstick kiss mark"></div>
    <div class="signature">Nora</div>
    <div class="divider"></div>

    <div class="dates">du sam 1 au sam 8<br>septembre 2018</div>
    <div class="postmark" role="img" aria-label="Postage stamp illustration"></div>
    <div class="place-tag"><span>Plage Morvane</span><span>Bulgarie</span></div>
    <div class="concept-tag">NEW<br>CONCEPT</div>
    <div class="offer">
      <span class="offer-title">ALL INCLUSIVE</span>
      <ul>
        <li>vol aller-retour</li>
        <li>hôtel 4****</li>
        <li>entrées en boites</li>
        <li>cocktails offerts</li>
        <li>beach party, ...</li>
        <li class="price">€ 599,00 / pers.</li>
      </ul>
    </div>
    <div class="bottom-strip"><span>www.golden-drift.example</span><span>0487 612 940</span></div>
  </section>

  <section class="card card-front" aria-label="Postcard front">
    <div class="stripe s1"></div>
    <div class="stripe s2"></div>
    <div class="stripe s3"></div>
    <div class="stripe s4"></div>
    <div class="photo p-girl" role="img" aria-label="Photo of a girl eating watermelon at the beach"></div>
    <div class="photo p-palm" role="img" aria-label="Photo of palm leaves in the sun"></div>
    <div class="photo p-jump" role="img" aria-label="Photo of a person jumping on the sand"></div>
    <div class="photo p-friends" role="img" aria-label="Photo of friends posing on the beach"></div>
    <div class="photo p-bag" role="img" aria-label="Photo of a straw beach bag"></div>
    <div class="hero">
      <div class="hero-title">Golden<br>Drift</div>
      <div class="hero-sub">Bulgaria 2018</div>
    </div>
    <div class="photo hero-photo" role="img" aria-label="Photo of friends sitting on the beach"></div>
    <div class="band"></div>
    <div class="agency"><span class="agency-dot"></span>MORELKA TRAVEL</div>
    <div class="front-concept">NEW<br>CONCEPT</div>
    <svg class="star" viewBox="0 0 30 30" aria-hidden="true">
      <polygon points="15,2 18.5,11 28,11 20.5,17 23.5,27 15,21 6.5,27 9.5,17 2,11 11.5,11" fill="#e8762b"/>
    </svg>
  </section>

</main>
</body>
</html>
```